Web Page Design for a Website that Provides Tutoring

I am looking to create an online tutoring website. The website will allow parents or students to contact tutors with a view to instructing them to tutor themselves or their children.

The name of the website is LendYourLessons.

This brief is to create the design for one of the web pages for this web site. I am hoping the same designer will be available to design other pages.

The page I want designed is one of the more complex and I have attached the design as an excel spreadsheet. The web page needs to include all the items on this page but if you want to change the positioning of the items then Im fine with that.

I recently had two logos created for this website. My favourite is the one with a mortar board but im not sure I like the colours. I have attached both of these logos and you can use either of them, change the colours or create something different. I just want a design pleasing to the eye. If the logo is changed I would like that in a seperate file.

So can you please submit designs for this page. I have attached the two logos which you can use, change or if you feel you have a better idea then you can use that.

On the spreadsheet the Send Message, Favourite etc are buttons.

Target Market(s)

People who want to better themselves.
Possible middle class to upper class.

Industry/Entity Type

Tutoring

Number of Pages Required

1 page

Requirements
Must have
• The designs must have alot of the information attached in the spreadsheet.

```html
<!DOCTYPE html>
<html lang="en">
<head>
<meta charset="utf-8">
<title>LendYourLessons – Tutoring</title>
<link rel="stylesheet" href="https://fonts.googleapis.com/css2?family=Jost:wght@400;500&family=Lato:wght@400;700&family=Oswald:wght@400;500&display=swap">
<style>
:root{
  --blue:#3a5a98;
  --orange:#f4683f;
  --ink:#333;
  --muted:#555;
  --grey-bg:#ececec;
  --card-grey:#e2e2e2;
  --table-head:#c9d3e0;
  --footer:#2e2e2e;
}
*{box-sizing:border-box;margin:0;padding:0}
html,body{width:1200px;height:2403px;overflow:hidden}
body{position:relative;font-family:"Lato",sans-serif;color:var(--ink);background:#fff}
.abs{position:absolute}
.btn{position:absolute;display:flex;align-items:center;justify-content:center;color:#fff;font-size:12px;background:var(--blue)}
.btn.orange{background:var(--orange)}
.heading{font-family:"Jost",sans-serif;font-weight:400;font-size:26px;text-align:center;color:var(--blue)}
.heading .accent{color:var(--orange)}
.divider{position:absolute;height:8px}

/* top bar */
.topbar{left:0;top:0;width:1200px;height:29px;background:var(--blue);color:#fff;font-size:12px}
.topbar .item{position:absolute;top:7px;display:flex;align-items:center;gap:8px}

/* header */
.brand{left:160px;top:62px;display:flex;align-items:center;gap:8px;font-weight:700;font-size:21px;color:var(--blue)}
.brand .mark{width:22px;height:22px;background:var(--orange)}
.nav a{position:absolute;top:70px;font-size:12px;color:#333;text-decoration:none;white-space:nowrap}
.nav a.active{color:var(--orange)}
.login{left:952px;top:62px;width:86px;height:28px}

/* hero */
.hero{left:0;top:117px;width:1200px;height:442px;overflow:hidden}
.hero-photo{left:0;top:0;width:700px;height:442px;background:linear-gradient(135deg,#1e2532 0%,#3a4356 45%,#c9bfae 80%,#ddd3c4 100%)}
.hero-text{left:640px;top:154px;width:410px;text-align:center;font-family:"Oswald",sans-serif;color:#fff;font-size:27px;line-height:37px;text-transform:uppercase}
.hero-btn{position:absolute;left:768px;top:278px;width:175px;height:39px;background:#fff;color:#222;font-family:"Oswald",sans-serif;font-size:17px;display:flex;align-items:center;justify-content:center}
.dots{left:826px;top:334px;display:flex;gap:5px}
.dots span{width:9px;height:9px;border-radius:50%;border:1.5px solid #fff}
.dots span.on{background:#fff}

/* about */
.about-avatar{left:160px;top:602px;width:149px;height:159px;background:var(--orange);padding:8px}
.about-avatar .portrait{width:133px;height:121px;background:linear-gradient(#f3f3f3,#dfe6f1)}
.about-avatar .caption{color:#fff;font-size:11px;font-weight:700;text-align:center;margin-top:6px}
.about-title{left:346px;top:600px;text-align:left}
.about-text{left:340px;top:653px;width:700px;font-size:12px;line-height:21px;color:var(--muted)}
.about-btn{left:340px;top:734px;width:86px;height:27px}

/* services */
.services-band{left:0;top:817px;width:1200px;height:295px;background:linear-gradient(180deg,#2c2b2a 0%,#54504a 50%,#3a3733 100%)}
.services-title{left:0;top:868px;width:1200px;color:#fff}
.card{position:absolute;top:985px;width:245px;height:190px;padding:16px;background:var(--card-grey)}
.card.orange{background:var(--orange)}
.card .inner{width:100%;height:100%;background:#fff;display:flex;align-items:center;justify-content:center}
.card-title{position:absolute;top:1204px;width:300px;text-align:center;font-family:"Jost",sans-serif;font-weight:500;font-size:14px;color:#222}
.card-text{position:absolute;top:1231px;width:300px;text-align:center;font-size:12px;line-height:19px;color:var(--muted)}
.card-btn{top:1302px;width:86px;height:28px}
.arrow{top:1058px}

/* reviews */
.reviews{left:0;top:1378px;width:1200px;height:357px;background:var(--grey-bg)}
.reviews-title{left:0;top:1430px;width:1200px}
.reviews-sub{left:0;top:1492px;width:1200px;text-align:center;font-size:15px;color:#333}
.review-table{left:160px;top:1533px;width:878px;border-collapse:collapse;font-size:14px;color:#666;background:#f4f4f4}
.review-table th{background:var(--table-head);font-family:"Jost",sans-serif;font-weight:400;font-size:17px;color:#333;text-align:left;height:40px;padding-left:64px;border:1px solid #b8b8b8}
.review-table td{height:36px;padding-left:64px;border:1px solid #c4c4c4}
.review-table td.score{color:var(--blue)}
.scrollbar{left:1031px;top:1573px;width:7px;height:109px;background:#e3e3e3}
.scrollbar i{position:absolute;left:0;top:39px;width:7px;height:26px;background:var(--blue)}

/* testimonial */
.testi-title{left:0;top:1784px;width:1200px}
.quote{left:160px;top:1855px;width:880px;height:132px}
.quote-text{left:190px;top:1862px;width:820px;text-align:center;font-size:12px;line-height:19px;color:var(--muted)}
.client-avatar{left:318px;top:1958px;width:56px;height:56px;border-radius:50%;border:2px solid var(--orange);background:linear-gradient(#f5f5f5,#dde4ef)}
.client-name{left:386px;top:1978px;font-size:13px;color:var(--orange)}
.client-city{left:516px;top:1978px;font-size:12px;color:#444}

/* footer */
.footer{left:0;top:2059px;width:1200px;height:299px;background:var(--footer)}
.f-head{position:absolute;top:2101px;font-family:"Jost",sans-serif;font-size:16px;color:#fff;padding-bottom:10px;border-bottom:1px solid #666}
.f-link{position:absolute;left:160px;font-size:12px;color:#fff}
.f-info{position:absolute;left:326px;font-size:12px;line-height:16px;color:#fff}
.field{position:absolute;left:567px;width:217px;background:#fff;font-size:11px;color:#999;padding:4px 5px}
.submit{left:569px;top:2286px;width:86px;height:27px}
.f-brand{left:849px;top:2243px;font-weight:700;font-size:22px;color:#cfcfcf}
.bottombar{left:0;top:2358px;width:1200px;height:45px;background:var(--blue);color:#fff;font-size:12px}
.social{position:absolute;top:11px;width:25px;height:25px;border-radius:50%;border:2px solid #fff}
.social.first{background:var(--orange)}
</style>
</head>
<body>

<div class="abs topbar">
  <div class="item" style="left:742px">
    <svg width="12" height="12" viewBox="0 0 24 24"><path fill="#fff" d="M6.6 10.8a15 15 0 006.6 6.6l2.2-2.2a1 1 0 011-.25 11.4 11.4 0 003.6.6 1 1 0 011 1V20a1 1 0 01-1 1A17 17 0 013 4a1 1 0 011-1h3.5a1 1 0 011 1 11.4 11.4 0 00.6 3.6 1 1 0 01-.25 1z"/></svg>
    123 456 7890
  </div>
  <div class="item" style="left:864px">
    <svg width="14" height="10" viewBox="0 0 14 10"><rect width="14" height="10" fill="#fff"/><path d="M0 0l7 5 7-5" stroke="#3a5a98" fill="none"/></svg>
    info@lendyourlessons.com
  </div>
</div>

<div class="abs brand"><span class="mark"></span>LendYourLessons</div>
<nav class="nav">
  <a class="active" style="left:505px">HOME</a>
  <a style="left:576px">ABOUT</a>
  <a style="left:653px">STUDENT</a>
  <a style="left:741px">TUTOR</a>
  <a style="left:815px">CONTACT</a>
</nav>
<svg class="abs" style="left:921px;top:67px" width="15" height="15" viewBox="0 0 15 15"><circle cx="6" cy="6" r="4.5" stroke="#555" stroke-width="1.6" fill="none"/><path d="M9.5 9.5L14 14" stroke="#555" stroke-width="1.8"/></svg>
<div class="btn login">
  <svg width="16" height="13" viewBox="0 0 16 13" style="margin-right:8px"><rect x="8" y="0" width="8" height="13" fill="#fff"/><path d="M0 6.5h7M4 3l3.5 3.5L4 10" stroke="#fff" stroke-width="2" fill="none"/></svg>Login
</div>

<section class="abs hero">
  <div class="abs hero-photo" role="img" aria-label="Photo from above of a student typing on a laptop at a desk"></div>
  <svg class="abs" style="left:0;top:0" width="1200" height="442" viewBox="0 0 1200 442"><path d="M633 0H1200V442H590C640 300 680 170 633 0Z" fill="#f4683f"/></svg>
  <div class="abs hero-text">Learn from<br>the best at your<br>pace &amp; your convenience</div>
  <div class="hero-btn">START NOW</div>
  <div class="abs dots"><span class="on"></span><span></span><span></span><span></span></div>
</section>

<div class="abs about-avatar">
  <div class="portrait" role="img" aria-label="Illustrated tutor portrait"></div>
  <div class="caption">Lorem Ipsum Dolor</div>
</div>
<h2 class="abs heading about-title">About <span class="accent">Lend Your Lessons</span></h2>
<svg class="divider" style="left:346px;top:637px" width="692" height="8"><path d="M0 4H692" stroke="#ccc"/></svg>
<p class="abs about-text">Lorem ipsum dolor sit amet, consectetuer adipiscing elit, sed diam nonummy nibh euismod tincidunt ut laoreet dolore magna aliquam erat volutpat. Ut wisi enim ad minim veniam, quis nostrud exerci tation ullamcorper suscipit lobortis nisl ut aliquip ex ea commodo consequat. Duis autem vel eum iriure dolor in hendrerit in vulputate velit esse molestie consequat, vel illum dolore eu feugiat.</p>
<div class="btn about-btn">Read More</div>

<div class="abs services-band" role="img" aria-label="Photo from above of students studying with laptops on a wooden floor"></div>
<h2 class="abs heading services-title" style="color:#fff">Our Services</h2>
<svg class="divider" style="left:503px;top:913px" width="194" height="8"><path d="M0 4H194" stroke="#ddd"/></svg>
<svg class="abs arrow" style="left:107px" width="20" height="30"><path d="M16 3L5 15l11 12" stroke="#fff" stroke-width="4" fill="none"/></svg>
<svg class="abs arrow" style="left:1072px" width="20" height="30"><path d="M4 3l11 12L4 27" stroke="#bbb" stroke-width="4" fill="none"/></svg>

<div class="card orange" style="left:160px" role="img" aria-label="Service frame: live video tutoring">
  <div class="inner"><svg width="60" height="44" viewBox="0 0 60 44"><rect x="0" y="0" width="44" height="30" rx="2" fill="#f4683f"/><circle cx="48" cy="24" r="7" fill="#f4683f"/><rect x="38" y="32" width="22" height="12" rx="5" fill="#f4683f"/></svg></div>
</div>
<div class="card" style="left:477px" role="img" aria-label="Service frame: student at a laptop">
  <div class="inner"><svg width="56" height="44" viewBox="0 0 56 44"><circle cx="12" cy="10" r="7" fill="#222"/><rect x="2" y="20" width="20" height="24" rx="4" fill="#222"/><path d="M28 6L52 12L46 36L22 30Z" fill="none" stroke="#222" stroke-width="3"/></svg></div>
</div>
<div class="card" style="left:794px" role="img" aria-label="Service frame: support agent with headset">
  <div class="inner"><svg width="48" height="48" viewBox="0 0 48 48"><circle cx="24" cy="16" r="10" fill="#222"/><path d="M10 18a14 14 0 0128 0" stroke="#222" stroke-width="3" fill="none"/><path d="M2 48a22 18 0 0144 0Z" fill="#222"/></svg></div>
</div>

<div class="card-title" style="left:134px">Live, One-On-One Tutoring</div>
<div class="card-title" style="left:457px">Available 24/7 For Many Subjects</div>
<div class="card-title" style="left:766px">Customized Service</div>
<p class="card-text" style="left:134px">sit amet, consectetuer adipiscing elit,<br>sed diam nonummy nsectetuer nibh<br>euismod tincidunt</p>
<p class="card-text" style="left:457px">sit amet, consectetuer adipiscing elit,<br>sed diam nonummy nsectetuer nibh<br>euismod tincidunt</p>
<p class="card-text" style="left:766px">sit amet, consectetuer adipiscing elit,<br>sed diam nonummy nsectetuer nibh<br>euismod tincidunt</p>
<div class="btn orange card-btn" style="left:241px">Read More</div>
<div class="btn card-btn" style="left:564px">Read More</div>
<div class="btn card-btn" style="left:873px">Read More</div>

<section class="abs reviews"></section>
<h2 class="abs heading reviews-title"><span class="accent">Tutor's</span> Name Reviews</h2>
<svg class="divider" style="left:503px;top:1472px" width="194" height="8"><path d="M0 4H194" stroke="#aaa"/></svg>
<p class="abs reviews-sub">Tutors Name Has 2 Reviews With An Average Review Of 4.0</p>
<table class="abs review-table">
  <colgroup><col style="width:260px"><col style="width:358px"><col style="width:260px"></colgroup>
  <tr><th>TUTEE NAME</th><th>DATE / TIME OF REVIEW</th><th>STAR RATEING 5.0</th></tr>
  <tr><td>Lorem Ipsum Dolor</td><td>Lorem Ipsum Dolor</td><td class="score">85%</td></tr>
  <tr><td>Lorem Ipsum Dolor</td><td>Lorem Ipsum Dolor</td><td class="score">85%</td></tr>
  <tr><td>Lorem Ipsum Dolor</td><td>Lorem Ipsum Dolor</td><td class="score">85%</td></tr>
</table>
<div class="abs scrollbar"><i></i></div>

<h2 class="abs heading testi-title"><span class="accent">Client</span> Testimonial</h2>
<svg class="divider" style="left:503px;top:1826px" width="194" height="8"><path d="M0 4H194" stroke="#ccc"/></svg>
<svg class="abs quote" viewBox="0 0 880 132"><path d="M12 .5H868a11.5 11.5 0 0111.5 11.5V76a11.5 11.5 0 01-11.5 11.5H190L150 110 145 87.5H12A11.5 11.5 0 01.5 76V12A11.5 11.5 0 0112 .5Z" fill="#fff" stroke="#ccc"/></svg>
<p class="abs quote-text">Lorem ipsum dolor sit amet, consectetuer adipiscing elit, sed diam nonummy nibh euismod tincidunt ut laoreet dolore magna aliquam erat volutpat. Ut wisi enim ad minim veniam, quis nostrud exerci tation ullamcorper suscipit lobortis nisl ut aliquip ex ea commodo consequat. Duis autem vel eum iriure dolor in hendrerit in vulputate velit esse molestie consequat, vel illum dolore eu</p>
<div class="abs client-avatar" role="img" aria-label="Client portrait"></div>
<div class="abs client-name">Lorem Ipsum Dolor</div>
<div class="abs client-city">New York</div>

<footer class="abs footer"></footer>
<div class="f-head" style="left:163px;width:94px">Quick Link</div>
<div class="f-head" style="left:328px;width:168px">Contact Info</div>
<div class="f-head" style="left:569px;width:215px">Quick Contact</div>
<div class="f-link" style="top:2150px">Home</div>
<div class="f-link" style="top:2179px">About</div>
<div class="f-link" style="top:2209px">Student</div>
<div class="f-link" style="top:2239px">Tutor</div>
<div class="f-link" style="top:2270px">Contact</div>
<div class="f-info" style="top:2150px">Lend Your Lessons<br>Lorem ipsum dolor sit amet,<br>consectetuer adipiscing elit<br>1234</div>
<div class="f-info" style="top:2232px;display:flex;gap:9px;align-items:center"><svg width="12" height="12" viewBox="0 0 24 24"><path fill="#fff" d="M6.6 10.8a15 15 0 006.6 6.6l2.2-2.2a1 1 0 011-.25 11.4 11.4 0 003.6.6 1 1 0 011 1V20a1 1 0 01-1 1A17 17 0 013 4a1 1 0 011-1h3.5a1 1 0 011 1 11.4 11.4 0 00.6 3.6 1 1 0 01-.25 1z"/></svg>123 456 7890</div>
<div class="f-info" style="top:2266px;display:flex;gap:9px;align-items:center"><svg width="14" height="10" viewBox="0 0 14 10"><rect width="14" height="10" fill="#fff"/><path d="M0 0l7 5 7-5" stroke="#2e2e2e" fill="none"/></svg>info@lendyourlessons.com</div>
<div class="field" style="top:2150px;height:26px">Name</div>
<div class="field" style="top:2185px;height:26px">Email</div>
<div class="field" style="top:2219px;height:56px">Message</div>
<div class="btn submit">Submit</div>
<div class="abs f-brand">LendYourLessons</div>

<div class="abs bottombar">
  <span class="abs" style="left:162px;top:15px">Copyright 16. Lend Your Lessons. All Right Reserved.</span>
  <span class="abs" style="left:833px;top:15px">Follow Us</span>
  <span class="social first" style="left:898px"></span>
  <span class="social" style="left:937px"></span>
  <span class="social" style="left:976px"></span>
  <span class="social" style="left:1013px"></span>
</div>

</body>
</html>
```